Willowmere Veterinary Practice including Nest2Nurse

We require a double-sided full colour tri-fold Brochure for Print.
Colour theme to in line with logo below

Written CONTENT below
Orphans
We can provide care and a new mother for orphan foals of any age, breed or size, from thoroughbreds and draft breeds to tiny ponies and even donkeys.
We have successfully fostered orphans from a few hours of age through to eight weeks, regardless of how long or if at all they were with their birth mother, and of previous fostering attempts.
We have the knowledge and experience to provide optimum nutrition and care to orphans during the brief period that they don’t have a mum, until their new foster mother is ready to take them.
Additionally we are a veterinary practice, and can provide diagnostics and therapeutics for compromised orphan foals such as plasma administration and health checks.

Mares
Nest2Nurse mares have been selected for mothering ability and temperament, and have all carried and raised at least one foal of their own. Many have already been successful foster mothers in one or more of the last five breeding seasons.
The mares are not currently pregnant and are given a carefully designed course of hormones to induce lactation when required. The milk produced is not colostrum, but is completely normal and equivalent to that which they would have had if the foal was theirs by birth.
There is published scientific information (in addition to our own experience and that of the owners of previous graduates of our programme) that growth and development of foals raised by induced lactation is identical to that of foals raised by their birth mothers.

Fostering
During the few days when the mare’s udder is developing, mare and foal are kept next separately but in close proximity, allowing bonding to begin and reducing stress on the orphan.
The fostering is completed once the mare has enough milk to feed the foal, and our experienced handlers ensure that joining the two goes smoothly.
Once they are together the mare completely accepts the foal as her own, and the foal can suckle freely – at this stage we continue to offer supplementary feeds until they are not needed.
The mare and foal are then a normal unit and can return to the foal owner’s care until weaning – ensuring optimum nutrition and behaviour for the foal and excellent outcomes in performance, relationships with other horses, and interaction with humans.

Complete Safety
Mares recognise their birth foal by scent - a unique bond established during the first few minutes of the foal’s life - and only a small percentage of mares who have lost their own foal will readily accept a substitute.
When a mare who has lost her birth foal is offered an orphan, it is very normal and common for her to respond with aggression - to the danger of the foal and the human handler.
Nest2Nurse mares have no birth foal in the current season, and are happy to adopt any foal who is placed close to them during the hormone treatment period.
This makes for total foal and handler safety.

Excellent Success Rate
After seven years of perfecting the fostering method, Nest2Nurse can claim total success: we have now documented almost 50 fosterings over the last five breeding seasons. We have never been entrusted with an orphan foal that we have not been able to provide with a beautiful foster mum.

Career Mothers
Being dedicated career mothers with no other job in life, our mares are free to accompany their new foals home and stay with them as long as required. No foals are weaned and left without a mother in our programme, and our beautiful mares who would otherwise not be bred, are given a foal every year and a wonderful lifelong purpose.

Every single orphan’s human family has admired and appreciated our beautiful mares, with many offering to give them a home for life. Each season as the orphans are weaned, we welcome our mares home to Willowmere to prepare for the next foal in need – a job they totally love! – just as if they were in a natural breeding situation.

Willowmere Vet Practice including Nest2Nurse
218 Pellbrook Lane
Tarrick. Vic. 3872

Phone 0491583620 or 0438261597

```html
<!DOCTYPE html>
<html lang="en">
<head>
<meta charset="utf-8">
<title>Nest2Nurse – Orphan Foal Fostering</title>
<link href="https://fonts.googleapis.com/css2?family=Open+Sans:wght@400;600;700;800&display=swap" rel="stylesheet">
<style>
  :root {
    --orange: #e8811f;
    --orange-deep: #d96f10;
    --wood-dark: #1f1d1c;
    --wood-mid: #353230;
    --paper: #f4f4f4;
    --paper-shade: #dcdcdc;
    --text-light: #f1f1f1;
    --text-dark: #3a3a3a;
  }
  * { box-sizing: border-box; margin: 0; padding: 0; }
  html, body { width: 1200px; height: 849px; overflow: hidden; background: #ffffff; }
  body { font-family: "Open Sans", Arial, sans-serif; }

  .brochure { position: relative; width: 1200px; height: 849px; display: flex; }

  .panel { position: relative; height: 849px; overflow: hidden; }
  .panel--orphans { width: 399px; background: linear-gradient(100deg, var(--wood-mid), var(--wood-dark) 60%, #2a2725); }
  .panel--mares { width: 399px; background: linear-gradient(90deg, var(--paper-shade) 0%, var(--paper) 12%, #ffffff 55%, var(--paper) 90%, var(--paper-shade) 100%); }
  .panel--safety { width: 402px; background: linear-gradient(95deg, #2c2927, var(--wood-dark) 50%, var(--wood-mid)); }

  .heading {
    font-weight: 700;
    font-size: 22px;
    letter-spacing: 0.3px;
    color: var(--orange);
    text-transform: uppercase;
    line-height: 1;
    margin-bottom: 8px;
  }
  .body-copy p {
    font-size: 13.2px;
    line-height: 17.6px;
    text-align: justify;
    margin-bottom: 17px;
  }
  .panel--orphans .body-copy p,
  .panel--safety .body-copy p { color: var(--text-light); }
  .panel--mares .body-copy p { color: var(--text-dark); }

  .hero-art { position: absolute; left: 0; top: 0; }

  .orphans-copy { position: absolute; left: 20px; top: 458px; width: 362px; }
  .mares-copy { position: absolute; left: 21px; top: 14px; width: 358px; }
  .mares-copy .section--fostering { margin-top: -2px; }
  .safety-copy { position: absolute; left: 20px; top: 14px; width: 358px; }
  .safety-copy .section--success { margin-top: -1px; }

  .foot-art { position: absolute; left: 0; bottom: 0; }
</style>
</head>
<body>
<main class="brochure">

  <section class="panel panel--orphans">
    <svg class="hero-art" width="399" height="520" viewBox="0 0 399 520">
      <defs>
        <linearGradient id="foalField" x1="0" y1="0" x2="0" y2="1">
          <stop offset="0" stop-color="#4a5a24"/>
          <stop offset="0.55" stop-color="#7d7a2e"/>
          <stop offset="1" stop-color="#a88a3a"/>
        </linearGradient>
        <linearGradient id="handlerScene" x1="0" y1="0" x2="1" y2="1">
          <stop offset="0" stop-color="#6b5a48"/>
          <stop offset="1" stop-color="#3b2f26"/>
        </linearGradient>
      </defs>
      <path role="img" aria-label="Young chestnut foal trotting across a sunlit paddock"
            d="M0 0 H399 V356 C300 372 160 410 0 440 Z" fill="url(#foalField)"/>
      <path d="M0 440 C160 410 300 372 399 356 V372 C300 390 160 428 0 458 Z" fill="var(--orange)"/>
      <circle cx="292" cy="423" r="90" fill="var(--orange)"/>
      <circle role="img" aria-label="Handler bottle-feeding an orphan foal in a stable" cx="292" cy="423" r="82" fill="url(#handlerScene)"/>
    </svg>

    <div class="orphans-copy body-copy">
      <h2 class="heading">Orphans</h2>
      <p>We can provide care and a new mother for orphan foals of any age, breed or size, from thoroughbreds and draft breeds to tiny ponies and even donkeys. We have successfully fostered orphans from a few hours of age through to eight weeks, regardless of how long or if at all they were with their birth mother, and of previous fostering attempts.</p>
      <p>We have the knowledge and experience to provide optimum nutrition and care to orphans during the brief period that they don’t have a mum, until their new foster mother is ready to take them.</p>
      <p>Additionally we are a veterinary practice, and can provide diagnostics and therapeutics for compromised orphan foals such as plasma administration and health checks.</p>
    </div>
  </section>

  <section class="panel panel--mares">
    <div class="mares-copy body-copy">
      <div class="section section--mares">
        <h2 class="heading">Mares</h2>
        <p>Nest2Nurse mares have been selected for mothering ability and temperament, and have all carried and raised at least one foal of their own. Many have already been successful foster mothers in one or more of the last five breeding seasons.</p>
        <p>The mares are not currently pregnant, and are given a carefully designed course of hormones to induce lactation when required. The milk produced is not colostrum, but is completely normal and equivalent to that which they would have had if the foal was theirs by birth.</p>
        <p>There is published scientific information (in addition to our own experience and that of the owners of previous graduates of our programme) that growth and development of foals raised by induced lactation is identical to that of foals raised by their birth mothers.</p>
      </div>
      <div class="section section--fostering">
        <h2 class="heading">Fostering</h2>
        <p>During the few days when the mare’s udder is developing, mare and foal are kept next separately but in close proximity, allowing bonding to begin and reducing stress on the orphan.</p>
        <p>The fostering is completed once the mare has enough milk to feed the foal, and our experienced handlers ensure that joining the two goes smoothly. Once they are together the mare completely accepts the foal as her own, and the foal can suckle freely – at this stage we continue to offer supplementary feeds until they are not needed.</p>
        <p>The mare and foal are then a normal unit and can return to the foal owner’s care until weaning – ensuring optimum nutrition and behaviour for the foal and excellent outcomes in performance, relationships with other horses, and interaction with humans.</p>
      </div>
    </div>
  </section>

  <section class="panel panel--safety">
    <div class="safety-copy body-copy">
      <div class="section section--safety">
        <h2 class="heading">Complete Safety</h2>
        <p>Mares recognise their birth foal by scent - a unique bond established during the first few minutes of the foal’s life - and only a small percentage of mares who have lost their own foal will readily accept a substitute.</p>
        <p>When a mare who has lost her birth foal is offered an orphan, it is very normal and common for her to respond with aggression - to the danger of the foal and the human handler.</p>
        <p>Nest2Nurse mares have no birth foal in the current season, and are happy to adopt any foal who is placed close to them during the hormone treatment period. This makes for total foal and handler safety.</p>
      </div>
      <div class="section section--success">
        <h2 class="heading">Excellent Success Rate</h2>
        <p>After seven years of perfecting the fostering method, Nest2Nurse can claim total success: we have now documented almost 50 fosterings over the last five breeding seasons. We have never been entrusted with an orphan foal that we have not been able to provide with a beautiful foster mum.</p>
      </div>
    </div>

    <svg class="foot-art" width="402" height="306" viewBox="0 0 402 306">
      <defs>
        <linearGradient id="mareFoal" x1="0" y1="0" x2="1" y2="1">
          <stop offset="0" stop-color="#b9b4a6"/>
          <stop offset="0.5" stop-color="#7a5a3e"/>
          <stop offset="1" stop-color="#3e2b1f"/>
        </linearGradient>
      </defs>
      <path d="M0 26 C120 6 260 0 402 6 V24 C260 18 120 24 0 44 Z" fill="var(--orange)"/>
      <path role="img" aria-label="Bay mare nuzzling her resting foster foal in a yard"
            d="M0 44 C120 24 260 18 402 24 V306 H0 Z" fill="url(#mareFoal)"/>
    </svg>
  </section>

</main>
</body>
</html>
```